CREATE A KILLER WEBSITE DESIGN

We are a firearms training company that trains CIVILIANS (no police or military pictures - thank you!) to defend themselves and are looking for a killer design that's clean, easy to navigate and modern! We want the newest trends applied to this sight like a scrollable site so you can scroll down and see all the features. We are okay with tweaking the HTML but need the artistic design to look good. I'll provide a link to our current site along with a sight we really like so you can get an idea!

I'm supplying a PowerPoint Design we are going with from another designer so you can match the style to the new site.

PAGES: (Please use information from our current site. We like the information but just want a more polished look similar to the NWDLA site below but in our colors.)
Home - Long Form Scrolling Site. Top fold will be a video with a play button.
Falcon Institute - Seven Level Training Program Info Page That Will Contain A Video.
Contact Us - This will be a page that DOES NOT CONTAIN AN EMAIL ADDRESS. Just a contact us form
Meet The Trainer: Morgan Pellbrook

Our site:
https://www.brisklanewardens.biz

Sights We Like:
https://www.nwdefenseleague.example.com
https://quorvel.example.com
https://brantforgeworks.example.com
https://www.pelnrigear.example.com

Target Market(s)

Men and women ages 21 to 100 years old

Industry/Entity Type

Self Defense

Number of Pages Required

5+ page

Font styles to use
Sans Serif

Colors
f26267

Requirements
Must have
• Clean and engaging. Use of colors that match our logo.
Should not have
• Poor design quality

```html
<!DOCTYPE html>
<html lang="en">
<head>
<meta charset="utf-8">
<title>Falcon Institute — Brisklane Wardens</title>
<link rel="stylesheet" href="https://fonts.googleapis.com/css2?family=Open+Sans:wght@400;600;700&family=Roboto:wght@500;700&display=swap">
<style>
:root{
  --red:#f05259;
  --red-soft:#f26267;
  --dark:#262626;
  --ink:#222;
  --text:#666;
  --grey-bg:#efefef;
  --pink-bg:#fde4e6;
  --white:#fff;
}
*{box-sizing:border-box;margin:0;padding:0}
html,body{width:1200px;height:4662px;overflow:hidden}
body{position:relative;font-family:"Open Sans",Arial,sans-serif;color:var(--text);background:var(--white)}
.abs{position:absolute}
h2,h3,.heading{font-family:"Roboto",Arial,sans-serif;font-weight:500;color:var(--ink)}
.btn-outline{position:absolute;border:2px solid var(--red);color:var(--red);font:600 14px "Open Sans",sans-serif;display:flex;align-items:center;justify-content:center;border-radius:3px;background:#fff}

/* top bar */
.topbar{top:0;left:0;width:1200px;height:112px;background:var(--red)}
.contact-line{left:112px;display:flex;align-items:center;gap:14px;color:#fff;font-size:14px;font-weight:600}
.icon-circle{width:30px;height:30px;border-radius:50%;background:#fff;display:flex;align-items:center;justify-content:center}
.brand-badge{left:500px;top:0;width:200px;height:112px}
.socials{right:112px;top:12px;display:flex;gap:12px}
.socials span{width:26px;height:26px;border-radius:50%;background:#fff;display:block}
.login{left:815px;top:62px;display:flex;align-items:center;gap:10px;color:#fff;font-size:14px;font-weight:600}
.tickets{left:930px;top:56px;width:158px;height:40px;border:1px solid #fff;color:#fff;font-size:13px;font-weight:600;display:flex;align-items:center;justify-content:center;border-radius:3px}

.mainnav{top:112px;left:0;width:1200px;height:51px;background:var(--dark)}
.mainnav ul{list-style:none;display:flex;gap:28px;position:absolute;left:112px;top:17px}
.mainnav li{color:#fff;font:700 14px "Open Sans",sans-serif}

/* hero */
.hero{top:163px;left:0;width:1200px;height:557px;background:linear-gradient(100deg,#2d3436 0%,#4f5a5c 30%,#8a7f6e 55%,#3e4a50 100%)}
.hero-shade{inset:0;background:rgba(0,0,0,.35)}
.hero h1{position:absolute;left:0;width:1200px;top:222px;text-align:center;color:#fff;font:500 25px/1.35 "Roboto",sans-serif}
.hero .sub{position:absolute;left:0;width:1200px;top:307px;text-align:center;color:#fff;font-size:13px;font-weight:700}
.hero .b1{left:380px;top:354px;width:188px;height:50px;border:2px solid #fff;color:#fff;font-size:13px;font-weight:700;display:flex;align-items:center;justify-content:center;border-radius:3px}
.hero .b2{left:589px;top:354px;width:230px;height:50px;background:var(--red);color:#fff;font-size:13px;font-weight:700;display:flex;align-items:center;justify-content:center;border-radius:3px}

/* about */
.about{top:720px;left:0;width:1200px;height:634px}
.about .frame{left:112px;top:85px;width:438px;height:448px;border:8px solid var(--red)}
.about .photo{left:147px;top:108px;width:440px;height:452px;background:linear-gradient(135deg,#d8d8d8,#6c6c6c);box-shadow:0 6px 14px rgba(0,0,0,.25)}
.about .kicker{left:630px;top:112px;font-size:14px;font-weight:700;color:var(--ink)}
.about h2{position:absolute;left:630px;top:138px;font-size:32px;color:var(--red)}
.about p{position:absolute;left:630px;top:190px;width:458px;font-size:14.4px;line-height:24.5px}
.about .btn-outline{left:630px;top:508px;width:150px;height:46px}

/* seen on */
.seen{top:1354px;left:0;width:1200px;height:432px;background:var(--red-soft);overflow:hidden}
.seen .deco{border-radius:50%;background:rgba(255,255,255,.06)}
.seen .kicker{left:0;width:1200px;top:70px;text-align:center;color:#fff;font-size:14px;font-weight:700}
.seen h2{position:absolute;left:0;width:1200px;top:92px;text-align:center;color:#fff;font-size:30px}
.outlet{width:192px;height:192px;border-radius:50%;background:#fff;top:162px;display:flex;align-items:center;justify-content:center;text-align:center;font:700 22px/1.1 "Open Sans",sans-serif;color:var(--ink)}

/* videos */
.videos h2{position:absolute;left:0;width:1200px;top:1864px;text-align:center;font-size:30px}
.video-frame{left:112px;top:1930px;width:976px;height:420px;background:radial-gradient(ellipse at center,#b3121b 0%,#7a0a10 60%,#4a0508 100%)}
.arrow{top:2126px}

/* levels */
.levels{top:2444px;left:0;width:1200px;height:781px;background:var(--grey-bg)}
.levels h2{position:absolute;left:0;width:1200px;top:88px;text-align:center;font-size:30px;line-height:36px}
.levels p{position:absolute;left:220px;width:760px;top:172px;text-align:center;font-size:14.4px;line-height:24px}
.levels .btn-outline{left:531px;top:645px;width:138px;height:50px;background:transparent}

/* stories */
.stories h2{position:absolute;left:0;width:1200px;top:3292px;text-align:center;font-size:30px}
.card{top:3357px;width:314px;height:334px;border:2px solid var(--red);background:#fff}
.card .face{left:0;top:0;width:110px;height:100px;background:linear-gradient(160deg,#e9e2dc,#a99a8f)}
.card h3{position:absolute;left:122px;top:36px;font-size:22px}
.card .date{left:122px;top:72px;font-size:11.5px}
.card p{position:absolute;left:30px;width:252px;top:140px;text-align:center;font-size:14.2px;line-height:24px}

/* contact */
.contact{top:3770px;left:0;width:1200px;height:538px;background:var(--pink-bg)}
.contact h2{position:absolute;top:80px;font-size:30px}
.contact .role{left:112px;top:138px;width:430px;font-size:15px;line-height:24px;text-transform:uppercase}
.info-row{left:112px;display:flex;align-items:center;gap:20px;font-size:14.5px;font-weight:600;color:var(--ink)}
.info-row .icon-circle{width:38px;height:38px;background:var(--red)}
.field{position:absolute;height:46px;border:2px solid #bbb;border-radius:4px;background:transparent;padding:12px 16px;font-size:14px;color:#888}
.submit{left:588px;top:418px;width:126px;height:42px;background:var(--red);color:#fff;font-weight:700;font-size:15px;display:flex;align-items:center;justify-content:center;border-radius:3px}

/* footer */
.footer{top:4308px;left:0;width:1200px;height:354px;background:var(--dark)}
.footer-brand{left:112px;top:150px;width:210px;text-align:center;color:#fff;font:700 26px/32px "Open Sans",sans-serif}
.footer h4{position:absolute;top:74px;color:#fff;font-size:15px;font-weight:700}
.footer ul{position:absolute;left:510px;top:128px;list-style:none}
.footer li{color:#fff;font-size:15px;line-height:25px}
.newsletter{left:860px;top:108px;width:228px;height:34px;border:1px solid #fff;border-radius:3px;color:#ccc;font-size:11px;padding:9px 14px}
.footer .rule{left:112px;top:304px;width:976px;height:1px;background:#555}
.footer .copy{left:0;width:1200px;top:320px;text-align:center;color:#fff;font-size:14px}
</style>
</head>
<body>

<header class="abs topbar">
  <div class="abs contact-line" style="top:12px">
    <span class="icon-circle"><svg width="16" height="16" viewBox="0 0 24 24"><path fill="#f05259" d="M6.6 10.8a15 15 0 0 0 6.6 6.6l2.2-2.2c.3-.3.7-.4 1-.2 1.1.4 2.3.6 3.6.6.6 0 1 .4 1 1V20c0 .6-.4 1-1 1A17 17 0 0 1 3 4c0-.6.4-1 1-1h3.5c.6 0 1 .4 1 1 0 1.3.2 2.5.6 3.6.1.3 0 .7-.2 1z"/></svg></span>
    555-014-BWRD (2291)
  </div>
  <div class="abs contact-line" style="top:60px">
    <span class="icon-circle"><svg width="16" height="16" viewBox="0 0 24 24"><rect x="3" y="6" width="18" height="12" rx="2" fill="none" stroke="#f05259" stroke-width="2"/><path d="M3 7l9 6 9-6" fill="none" stroke="#f05259" stroke-width="2"/></svg></span>
    hello@brisklanewardens.example.com
  </div>
  <svg class="abs brand-badge" viewBox="0 0 200 112">
    <polygon points="30,0 170,0 200,112 0,112" fill="#fff"/>
    <text x="100" y="60" text-anchor="middle" font-family="Open Sans, sans-serif" font-weight="700" font-size="19" fill="#262626">FALCON</text>
    <text x="100" y="84" text-anchor="middle" font-family="Open Sans, sans-serif" font-weight="700" font-size="19" fill="#262626">INSTITUTE</text>
  </svg>
  <div class="abs socials" aria-hidden="true"><span></span><span></span><span></span><span></span></div>
  <div class="abs login">
    <span class="icon-circle"><svg width="14" height="14" viewBox="0 0 24 24"><circle cx="12" cy="8" r="4" fill="#f05259"/><path d="M4 21c0-4.4 3.6-7 8-7s8 2.6 8 7z" fill="#f05259"/></svg></span>
    LOGIN
  </div>
  <div class="abs tickets">GET TICKETS NOW</div>
</header>

<nav class="abs mainnav">
  <ul>
    <li>HOME</li><li>ABOUT</li><li>FALCON INSTITUTE</li><li>UPCOMING CLASSES</li><li>SHOP</li><li>VIDEOS</li><li>LOST CERTIFICATES</li><li>TESTIMONIALS</li>
  </ul>
</nav>

<section class="abs hero">
  <div class="abs" style="inset:0" role="img" aria-label="Video still of a civilian student aiming a handgun at targets on an indoor range"></div>
  <div class="abs hero-shade"></div>
  <svg class="abs" style="left:584px;top:153px" width="32" height="32" viewBox="0 0 32 32"><polygon points="2,2 30,16 2,30" fill="#f05259"/></svg>
  <h1>YOUR LIFE MAY DEPEND ON WHAT YOU LEARN IN YOUR<br>CONCEALED CARRY TRAINING</h1>
  <div class="sub">DON'T SETTLE FOR A GUN SHOP CLASS!</div>
  <div class="abs b1">FALCON INSTITUTE</div>
  <div class="abs b2">I NEED IMMEDIATE SERVICE</div>
</section>

<section class="abs about">
  <div class="abs frame"></div>
  <div class="abs photo" role="img" aria-label="Black and white portrait of instructor Morgan Pellbrook"></div>
  <div class="abs kicker">ABOUT THE INSTRUCTOR</div>
  <h2>MORGAN PELLBROOK</h2>
  <p>Morgan Pellbrook is a 3rd generation Harlow Point native and delighted to be a part of this great community. He is a true security expert with 25 years of experience in the security industry. He has appeared on Harbor, Crestline, Northway &amp; Meridian news outlets. He has been Featured in numerous publications and has trained thousands to protect themselves and their homes from thugs and thieves. He is certified by both the CRL &amp; the NWDLA as a firearms instructor. He is also an CRL Range Safety Officer and Defensive Pistol Instructor. He often says: "My students are like family so I take their security personal. I want them to feel confident that they can protect themselves and their families!"</p>
  <div class="btn-outline">LEARN MORE</div>
</section>

<section class="abs seen">
  <div class="abs deco" style="left:390px;top:60px;width:110px;height:110px"></div>
  <div class="abs deco" style="left:880px;top:-60px;width:360px;height:360px"></div>
  <div class="abs kicker">OUR CLIENTS</div>
  <h2>AS SEEN ON</h2>
  <div class="abs outlet" style="left:112px">Harbor<br>News</div>
  <div class="abs outlet" style="left:373px">Meridian<br>News</div>
  <div class="abs outlet" style="left:634px;background:#efefef">Crestline<br>TV</div>
  <div class="abs outlet" style="left:896px">Northway<br>7</div>
</section>

<section class="videos">
  <h2>OUR VIDEOS</h2>
  <div class="abs video-frame" role="img" aria-label="Video cover with the slogan Real Training, Real Results in distressed lettering"></div>
  <svg class="abs" style="left:580px;top:2122px" width="40" height="40" viewBox="0 0 40 40"><polygon points="4,2 38,20 4,38" fill="#f05259"/></svg>
  <svg class="abs arrow" style="left:70px" width="20" height="30" viewBox="0 0 20 30"><polyline points="16,2 4,15 16,28" fill="none" stroke="#222" stroke-width="3"/></svg>
  <svg class="abs arrow" style="left:1110px" width="20" height="30" viewBox="0 0 20 30"><polyline points="4,2 16,15 4,28" fill="none" stroke="#f05259" stroke-width="3"/></svg>
</section>

<section class="abs levels">
  <h2>OUR 7 LEVELS OF TRAINING TAKE YOU FROM<br>ZERO TO HERO</h2>
  <p>Wanna hear something funny? Guess what the average person asks about a concealed weapons class? "How much is it and how long is it?" Can you believe it? We are talking about preparing you for life and death situations and the main concern is "How Fast" and "How Cheap?" WOW!</p>
  <svg class="abs" style="left:0;top:280px" width="1200" height="340" viewBox="0 0 1200 340" font-family="Open Sans, sans-serif">
    <g stroke="#f05259" stroke-width="2">
      <line x1="308" y1="22" x2="308" y2="100"/><line x1="583" y1="22" x2="583" y2="100"/><line x1="858" y1="22" x2="858" y2="100"/>
      <line x1="170" y1="218" x2="170" y2="298"/><line x1="445" y1="218" x2="445" y2="298"/><line x1="720" y1="218" x2="720" y2="298"/><line x1="997" y1="218" x2="997" y2="298"/>
    </g>
    <g fill="#f05259">
      <circle cx="308" cy="22" r="7"/><circle cx="583" cy="22" r="7"/><circle cx="858" cy="22" r="7"/>
      <circle cx="170" cy="298" r="7"/><circle cx="445" cy="298" r="7"/><circle cx="720" cy="298" r="7"/><circle cx="997" cy="298" r="7"/>
    </g>
    <g font-size="10" font-weight="700" fill="#555">
      <text x="320" y="50">DYNAMIC DEFENSIVE</text><text x="350" y="68">SHOOTING</text>
      <text x="593" y="50">VIRTUAL THREAT-LAB</text>
      <text x="873" y="50">CLOSE QUARTERS</text><text x="898" y="68">DEFENSE</text>
      <text x="185" y="250">CONCEALED</text><text x="185" y="268">CARRY CLASS</text>
      <text x="458" y="252">FINE TUNING YOUR</text><text x="478" y="270">TECHNIQUE</text>
      <text x="737" y="252">TACTICAL SKILLS &amp;</text><text x="770" y="270">DRILLS</text>
      <text x="1012" y="252">LIVE SCENARIO</text><text x="1020" y="270">THREAT-LAB</text>
    </g>
    <g>
      <g transform="translate(170,159)"><circle r="60" fill="#f05259"/><circle r="46" fill="#fff"/><text y="5" text-anchor="middle" font-size="13" font-weight="600" fill="#f05259">LEVEL 01</text></g>
      <g transform="translate(308,159)"><circle r="60" fill="#f05259"/><circle r="46" fill="#fff"/><text y="5" text-anchor="middle" font-size="13" font-weight="600" fill="#f05259">LEVEL 02</text></g>
      <g transform="translate(445,159)"><circle r="60" fill="#f05259"/><circle r="46" fill="#fff"/><text y="5" text-anchor="middle" font-size="13" font-weight="600" fill="#f05259">LEVEL 03</text></g>
      <g transform="translate(583,159)"><circle r="60" fill="#f05259"/><circle r="46" fill="#fff"/><text y="5" text-anchor="middle" font-size="13" font-weight="600" fill="#f05259">LEVEL 04</text></g>
      <g transform="translate(720,159)"><circle r="60" fill="#f05259"/><circle r="46" fill="#fff"/><text y="5" text-anchor="middle" font-size="13" font-weight="600" fill="#f05259">LEVEL 05</text></g>
      <g transform="translate(858,159)"><circle r="60" fill="#f05259"/><circle r="46" fill="#fff"/><text y="5" text-anchor="middle" font-size="13" font-weight="600" fill="#f05259">LEVEL 06</text></g>
      <g transform="translate(997,159)"><circle r="60" fill="#f05259"/><circle r="46" fill="#fff"/><text y="5" text-anchor="middle" font-size="13" font-weight="600" fill="#f05259">LEVEL 07</text></g>
    </g>
  </svg>
  <div class="btn-outline">LEARN MORE</div>
</section>

<section class="stories">
  <h2>SUCCESS STORIES</h2>
  <article class="abs card" style="left:112px">
    <div class="abs face" role="img" aria-label="Headshot of student Renata M"></div>
    <h3>RENATA M</h3><div class="abs date">October 14, 2017</div>
    <p>"I had never held a gun when I took the Brisklane Wardens class and I'm hooked! I'm going all the way to level 7! Thank you Brisklane Wardens!</p>
  </article>
  <article class="abs card" style="left:443px">
    <div class="abs face" role="img" aria-label="Headshot of student Delphine S"></div>
    <h3>DELPHINE S</h3><div class="abs date">December 9, 2017</div>
    <p>"I was mugged here in Harlow Point and lived in fear ever since. It stole my happiness and I became scared to go out. I'm a Level 4 student and I feel sorry for the next thug that tries me!"</p>
  </article>
  <article class="abs card" style="left:773px">
    <div class="abs face" role="img" aria-label="Headshot of student Walt G"></div>
    <h3>WALT G</h3><div class="abs date">March 3 2018</div>
    <p>"I've been shooting for years and already had my concealed weapons license. My first class was a gun shop class and a waste of money. Morgan took the time to show me how to properly grip my gun and my shooting dramatically improved!</p>
  </article>
</section>

<section class="abs contact">
  <h2 style="left:112px">MORGAN PELLBROOK</h2>
  <div class="abs role">CRL Firearms Instructor, NWDLA Instructor &amp; Training Counsellor, News Correspondent, and Security Expert</div>
  <div class="abs info-row" style="top:228px">
    <span class="icon-circle"><svg width="16" height="18" viewBox="0 0 24 28"><path d="M12 1a9 9 0 0 0-9 9c0 7 9 17 9 17s9-10 9-17a9 9 0 0 0-9-9z" fill="#fff"/><circle cx="12" cy="10" r="3.5" fill="#f05259"/></svg></span>
    <span>P.O. Box 4410<br>Harlow Point, FL 32990</span>
  </div>
  <div class="abs info-row" style="top:294px">
    <span class="icon-circle"><svg width="16" height="16" viewBox="0 0 24 24"><path fill="#fff" d="M6.6 10.8a15 15 0 0 0 6.6 6.6l2.2-2.2c.3-.3.7-.4 1-.2 1.1.4 2.3.6 3.6.6.6 0 1 .4 1 1V20c0 .6-.4 1-1 1A17 17 0 0 1 3 4c0-.6.4-1 1-1h3.5c.6 0 1 .4 1 1 0 1.3.2 2.5.6 3.6.1.3 0 .7-.2 1z"/></svg></span>
    555-014-BWRD (2291)
  </div>
  <div class="abs info-row" style="top:354px">
    <span class="icon-circle"><svg width="16" height="16" viewBox="0 0 24 24"><rect x="3" y="6" width="18" height="12" rx="2" fill="none" stroke="#fff" stroke-width="2"/><path d="M3 7l9 6 9-6" fill="none" stroke="#fff" stroke-width="2"/></svg></span>
    hello@brisklanewardens.example.com
  </div>

  <h2 style="left:588px">GET IN TOUCH</h2>
  <div class="field" style="left:588px;top:140px;width:240px">First Name</div>
  <div class="field" style="left:845px;top:140px;width:241px">Last Name</div>
  <div class="field" style="left:588px;top:206px;width:240px">Email</div>
  <div class="field" style="left:845px;top:206px;width:241px">Phone Number</div>
  <div class="field" style="left:588px;top:274px;width:498px;height:116px">Message</div>
  <div class="abs submit">SUBMIT</div>
</section>

<footer class="abs footer">
  <div class="abs footer-brand">BRISKLANE<br>WARDENS</div>
  <h4 style="left:510px">QUICK LINKS</h4>
  <ul><li>Home</li><li>About</li><li>Falcon Institute</li><li>Upcoming Classes</li><li>Shop</li><li>Videos</li><li>Lost Certificate</li></ul>
  <h4 style="left:860px">NEWSLETTER</h4>
  <div class="abs newsletter">Enter your email</div>
  <svg class="abs" style="left:1054px;top:118px" width="16" height="16" viewBox="0 0 24 24"><path d="M2 12l20-9-7 19-3-8z" fill="none" stroke="#fff" stroke-width="2"/></svg>
  <div class="abs rule"></div>
  <div class="abs copy">© 2021 Brisklane Wardens. All Rights Reserved.</div>
</footer>

</body>
</html>
```